Vuntrelo - In Need of Logo/Packaging Design

I am looking for a logo and packaging design for my new company, "Vuntrelo". Vuntrelo is monthly subscription box that delivers golf equipment and accessories directly to the customer's door. The box will be a standard craft material Roll End Front Tuck mailer - the dimensions of the box are as follows:

9"x12"x3.5" (LxWxH)

I would like to see a simple and modern design that ultimately communicates innovation and creativity with the sport of golf. The box will be standard craft cardboard material therefore I would like to incorporate colors with good contrast; I am visualizing black/gray/white but am open to other options as well. If possible I would also like to incorporate the following slogan in some way:

Reliability & Convenience

I've attached a couple logos that I found online which I really like so you can get an idea of what I am looking for.

Thank you!

Target Market(s)

The upcoming young, millennial golfer.

Industry/Entity Type

Sporting Good

Logo Text

Vuntrelo

Requirements
Must have
• Logo/packaging design

```html
<!DOCTYPE html>
<html lang="en">
<head>
<meta charset="utf-8">
<title>Vuntrelo – Mailer Box Dieline</title>
<link href="https://fonts.googleapis.com/css2?family=Heebo:wght@400;700;800&family=Open+Sans:wght@400;600&display=swap" rel="stylesheet">
<style>
  :root{
    --stage:#fdfa7c;
    --kraft:#c08f5f;
    --kraft-light:#d7b088;
    --ink:#0b0b0b;
    --slate:#585d5c;
    --paper:#ffffff;
    --fold:#e9d5bf;
  }
  html,body{margin:0;padding:0;overflow:hidden;background:var(--stage);}
  .canvas{position:relative;width:1200px;height:1200px;overflow:hidden;background:var(--stage);font-family:"Open Sans",sans-serif;}
  .dieline{position:absolute;inset:0;}
  .heading{font-family:"Heebo",sans-serif;font-weight:700;fill:var(--ink);}
  .caption{font-family:"Open Sans",sans-serif;fill:var(--ink);}
  .caption--light{fill:var(--paper);}
  .brand{font-family:"Heebo",sans-serif;font-weight:800;fill:var(--ink);}
  .body-copy{position:absolute;font-family:"Open Sans",sans-serif;font-size:4.6px;line-height:6.4px;color:var(--ink);text-align:justify;margin:0;}
  .body-copy p{margin:0 0 5px;}
  .contact-card{position:absolute;left:636px;top:425px;width:138px;height:58px;border:1px solid var(--slate);box-sizing:border-box;font-family:"Open Sans",sans-serif;font-size:5px;font-weight:600;color:var(--ink);padding:9px 0 0 22px;}
  .contact-card__title{margin:0 0 7px 12px;}
  .contact-card__row{display:flex;align-items:center;gap:4px;margin-bottom:4px;}
  .contact-card__icon{width:5px;height:5px;border:1px solid var(--ink);border-radius:1px;box-sizing:border-box;}
</style>
</head>
<body>
<div class="canvas">
<svg class="dieline" width="1200" height="1200" viewBox="0 0 1200 1200" xmlns="http://www.w3.org/2000/svg">
  <defs>
    <radialGradient id="dimple-tone" cx="50%" cy="50%" r="50%">
      <stop offset="0" stop-color="#cfa77b"/>
      <stop offset="0.75" stop-color="#c99f73"/>
      <stop offset="1" stop-color="#c08f5f"/>
    </radialGradient>
    <clipPath id="clip-top-flap"><path d="M256 14H944V145L930 158H270L256 145Z"/></clipPath>
    <clipPath id="clip-body"><rect x="69" y="158" width="1061" height="370"/></clipPath>
    <clipPath id="clip-lid-front"><path d="M256 528H944V664H256Z"/></clipPath>
    <clipPath id="clip-base"><path d="M258 700L350 672H850L944 700V1020L850 1044H350L258 1020Z"/></clipPath>
    <clipPath id="clip-tuck"><path d="M300 1040H900Q936 1040 936 1090V1130Q936 1184 880 1184H320Q264 1184 264 1130V1090Q264 1040 300 1040Z"/></clipPath>
    <g id="flap-waves">
      <path fill="var(--slate)" d="M300 160C330 112 420 86 540 90C700 98 770 140 860 112C905 96 930 62 946 12L946 160Z"/>
      <path fill="var(--ink)" d="M350 160C392 122 472 110 562 116C720 126 800 152 882 130C922 116 940 92 946 66L946 160Z"/>
    </g>
  </defs>

  <!-- Top flap -->
  <g class="panel panel--top-flap" clip-path="url(#clip-top-flap)">
    <rect x="256" y="14" width="688" height="144" fill="var(--kraft)"/>
    <use href="#flap-waves"/>
    <text class="caption" x="403" y="46" font-size="13">Monthly Subscription Box</text>
    <text class="caption caption--light" x="403" y="141" font-size="9.5">Golf Equipment &amp; Accessories</text>
    <text class="brand" x="702" y="90" font-size="24" text-anchor="middle">Vuntrelo</text>
  </g>

  <!-- Main body strip -->
  <g class="panel panel--body">
    <rect x="66" y="226" width="4" height="40" fill="var(--kraft)"/>
    <rect x="66" y="402" width="4" height="40" fill="var(--kraft)"/>
    <rect x="1130" y="226" width="4" height="40" fill="var(--kraft)"/>
    <rect x="1130" y="402" width="4" height="40" fill="var(--kraft)"/>
    <rect x="69" y="158" width="1061" height="370" fill="var(--kraft)"/>
    <g clip-path="url(#clip-body)">
      <ellipse role="img" aria-label="Soft golf ball dimple texture" cx="560" cy="585" rx="200" ry="140" fill="url(#dimple-tone)"/>
    </g>
    <line x1="212" y1="158" x2="212" y2="528" stroke="var(--fold)" stroke-width="1"/>
    <line x1="990" y1="158" x2="990" y2="528" stroke="var(--fold)" stroke-width="1"/>
    <rect x="349" y="225" width="3" height="40" fill="none" stroke="var(--fold)"/>
    <rect x="349" y="402" width="3" height="40" fill="none" stroke="var(--fold)"/>
    <rect x="848" y="225" width="3" height="40" fill="none" stroke="var(--fold)"/>
    <rect x="848" y="402" width="3" height="40" fill="none" stroke="var(--fold)"/>

    <text class="heading" font-size="13" transform="translate(311 293) rotate(-90)">Golf Equipment &amp;</text>
    <text class="heading" font-size="13" transform="translate(327 293) rotate(-90)">Accessories</text>
    <text class="brand" font-size="22" text-anchor="middle" transform="translate(292 404) rotate(-90)">Vuntrelo</text>

    <text class="heading" x="393" y="214" font-size="18.5">Golf Equipment &amp;</text>
    <text class="heading" x="393" y="236" font-size="18.5">Accessories</text>

    <text class="brand" x="702" y="254" font-size="24" text-anchor="middle">Vuntrelo</text>

    <text class="brand" font-size="22" text-anchor="middle" transform="translate(910 262) rotate(90)">Vuntrelo</text>
    <text class="heading" font-size="13" transform="translate(895 394) rotate(90)">Golf Equipment &amp;</text>
    <text class="heading" font-size="13" transform="translate(879 394) rotate(90)">Accessories</text>

    <rect x="396" y="488" width="22" height="20" rx="2" fill="none" stroke="var(--slate)" stroke-width="1.2"/>
    <rect x="432" y="488" width="22" height="20" rx="2" fill="none" stroke="var(--slate)" stroke-width="1.2"/>
  </g>

  <!-- Lid front -->
  <g class="panel panel--lid-front" clip-path="url(#clip-lid-front)">
    <rect x="256" y="528" width="688" height="136" fill="var(--kraft)"/>
    <circle role="img" aria-label="Soft golf ball dimple texture" cx="550" cy="740" r="290" fill="url(#dimple-tone)"/>
    <g transform="rotate(180 600 343)">
      <use href="#flap-waves"/>
      <text class="caption" x="410" y="46" font-size="13">Monthly Subscription Box</text>
      <text class="caption caption--light" x="410" y="145" font-size="9.5">Golf Equipment &amp; Accessories</text>
      <text class="brand" x="692" y="90" font-size="24" text-anchor="middle" fill="var(--ink)">Vuntrelo</text>
    </g>
  </g>

  <!-- Base panel -->
  <g class="panel panel--base" clip-path="url(#clip-base)">
    <rect x="256" y="664" width="690" height="384" fill="var(--kraft)"/>
    <circle role="img" aria-label="Large golf ball dimple texture" cx="550" cy="740" r="290" fill="url(#dimple-tone)"/>
    <text class="heading" x="403" y="723" font-size="18.5">Golf Equipment &amp; Accessories</text>
    <text class="caption" x="403" y="743" font-size="13">Monthly Subscription Box</text>
    <text class="brand" x="702" y="918" font-size="40" text-anchor="middle">Vuntrelo</text>
  </g>

  <!-- Tuck flap -->
  <g class="panel panel--tuck" clip-path="url(#clip-tuck)">
    <rect x="264" y="1040" width="672" height="144" fill="var(--kraft)"/>
    <g transform="translate(-10 1026)"><use href="#flap-waves"/></g>
    <text class="caption" x="403" y="1070" font-size="13">Monthly Subscription Box</text>
    <text class="caption caption--light" x="403" y="1165" font-size="9.5">Golf Equipment &amp; Accessories</text>
    <text class="brand" x="702" y="1114" font-size="24" text-anchor="middle">Vuntrelo</text>
  </g>
</svg>

<div class="body-copy" style="left:393px;top:272px;width:124px;">
  <p>I am looking for a logo and packaging design for my new company, "Vuntrelo". Vuntrelo is monthly subscription box that delivers golf equipment and accessories directly to the customer's door. The box will be a standard craft material Roll End Front Tuck mailer - the dimensions of the box are as follows:</p>
  <p>9"x12"x3.5" (LxWxH)</p>
  <p>I would like to see a simple and modern design that ultimately communicates innovation and creativity with the sport of golf. The box will be standard craft cardboard material therefore I would like to incorporate colors with good contrast; I am visualizing black/gray/white but am open to other options as well. If possible I would also like to incorporate the following slogan in some way:</p>
  <p>Reliability &amp; Convenience</p>
  <p>I've attached a couple logos that I found online which I really like so you can get an idea of what I am looking for.</p>
</div>

<div class="body-copy" style="left:644px;top:315px;width:122px;">
  <p>I am looking for a logo and packaging design for my new company, "Vuntrelo". Vuntrelo is monthly subscription box that delivers golf equipment and accessories directly to the customer's door. The box will be a standard craft material Roll End Front Tuck mailer - the dimensions of the box are as follows:</p>
  <p>9"x12"x3.5" (LxWxH)</p>
  <p>I would like to see a simple and modern design that ultimately communicates innovation and creativity with the sport of golf. The box will be standard craft cardboard material therefore I would like to incorporate colors with good contrast; I am visualizing</p>
</div>

<div class="contact-card">
  <p class="contact-card__title">This Materials are sent by: Vuntrelo</p>
  <div class="contact-card__row"><span class="contact-card__icon"></span>+1-800-555-0147</div>
  <div class="contact-card__row"><span class="contact-card__icon"></span>hello@vuntrelo.example</div>
  <div class="contact-card__row"><span class="contact-card__icon"></span>www.vuntrelo.example</div>
</div>
</div>
</body>
</html>
```